Design a great website for our amazing new country club in Southern California!

Our old neighborhood golf club is being transformed into a 100% new world-class club located down the street from the old location. We want a new website look that projects our new image. However because the club hasn't been built yet, we don't have a lot of images--just a new logo and a few renderings. So we will add images in the coming months as things get built. In the meantime, for things such as restaurant or swimming or tennis pics, feel free to plug in stock internet images for now. And regarding the movie file, we had an idea for a dramatic headline slowly rising over the clubhouse. It's just an idea, however, we're not married to it. We need to get creative here, as we have so few images. Oh, and we definitely want one main graphic on the home page. We don't like the slide-show effect--looks cheap. And finally, the landing page will be a 'public' page with other pages aimed at attracting new members. There will also be a 'Members area' that is password-protected. Site maps and rough copy for each of the two sections is included. Good luck!! :-) Please view our current website: sagemeadowcc.com

Wealthy folks who like golf, sports and dining. Our memberships range in price from $18,000 to $130,000.

Club

Coded - Design and coding required

5+ page

Sans Serif

• a GORGEOUS home page, with buttons and features that will remain static on all other pages. We want the navigation buttons along the top with pull-downs. Only the areas below the nav buttons will change. We want this site to look very clean and classy.
• Maybe have the button 'glow' or enlarge or whatever when you roll over them. Whatever can spruce up the simple classy design. Maybe so some special effect to the SM logo as well. As long as it looks classy, that's the main thing. And if you can find some good generic images of golf, dining, swimming, tennis, whatever on the net, feel free to use them.
• No slide show effects, with multiple images changing.

```html
<!DOCTYPE html>
<html lang="en">
<head>
<meta charset="utf-8">
<title>Sage Meadow Country Club</title>
<link href="https://fonts.googleapis.com/css2?family=Marcellus&family=Open+Sans:ital,wght@0,400;0,600;1,400&display=swap" rel="stylesheet">
<style>
:root{
  --ink:#231f20;
  --dark:#282425;
  --green:#5aa51c;
  --green-text:#6cae2a;
  --paper:#ffffff;
  --muted:#555;
  --footer-text:#d8d8d8;
  --bar:#e6e6e6;
}
*{margin:0;padding:0;box-sizing:border-box}
html,body{width:788px;height:1200px;overflow:hidden;background:var(--paper)}
body{position:relative;font-family:"Open Sans",sans-serif;color:var(--ink)}
.abs{position:absolute}
.serif{font-family:"Marcellus",serif}

.hero{left:0;top:0;width:788px;height:278px;background:linear-gradient(180deg,#6f8a6c 0%,#8fa57e 30%,#b8a58c 55%,#7fb3c9 75%,#9fb08a 100%)}
.hero-brand{left:340px;top:0;width:109px;height:84px;background:var(--paper);display:flex;flex-direction:column;align-items:center;justify-content:center;gap:5px}
.brand-mark{width:18px;height:18px;background:var(--ink)}
.hero-brand .brand-name{font-family:"Marcellus",serif;font-size:11px;color:var(--ink);text-align:center;line-height:1.2}
.headline{left:188px;top:126px;width:412px;height:52px;background:rgba(35,31,32,.9);color:#fff;text-align:center;text-transform:uppercase;font-weight:400}
.headline .l1{display:block;font-size:20px;letter-spacing:.5px;padding-top:7px;line-height:22px}
.headline .l2{display:block;font-size:12px;line-height:16px}
.scroll{left:379px;top:214px;width:30px;height:50px;border-radius:15px;background:#fff;border:2px solid #ccc;font-size:7px;text-align:center;padding-top:22px;line-height:8px}
.scroll::before{content:"";position:absolute;left:9px;top:7px;width:9px;height:9px;border-radius:50%;border:2px solid var(--green)}

.nav{left:0;top:278px;width:788px;height:36px;background:#fff;border-bottom:1px solid #eee}
.nav-brand{left:138px;top:9px;display:flex;align-items:center;gap:6px}
.nav-brand .brand-mark{width:16px;height:16px}
.nav-brand .brand-name{font-family:"Marcellus",serif;font-size:13px}
.nav-links{right:136px;top:12px;display:flex;gap:10px;list-style:none;font-family:"Marcellus",serif;font-size:8px;text-transform:uppercase;color:var(--ink)}

.intro{left:144px;top:338px;width:500px;text-align:center}
.intro h2{font-style:italic;font-weight:400;color:var(--green-text);font-size:14px;line-height:18px;margin-bottom:8px}
.intro p{font-size:7px;line-height:10px;color:var(--muted)}
.intro p.lead{font-size:9px;line-height:12px;color:#444;margin-bottom:6px}
.rendering{left:145px;top:446px;width:497px;height:214px;background:linear-gradient(180deg,#eef3ea 0%,#c9d6b2 45%,#9bb56e 100%)}
.established{left:0;top:666px;width:788px;text-align:center;font-size:11px;color:#444}

.features{left:0;top:690px;width:788px;height:200px;background:var(--dark)}
.card{top:30px;width:166px;height:138px;border:1px solid #777;display:flex;flex-direction:column;align-items:center;justify-content:center;color:#fff;text-align:center}
.card h3{font-family:"Marcellus",serif;font-weight:400;font-size:14px;text-transform:uppercase;line-height:15px;margin-bottom:12px;display:flex;align-items:center;gap:5px}
.card h3 span{white-space:nowrap}
.card h3::before,.card h3::after{content:"";flex:none;width:18px;height:4px;border-top:1px solid #fff;border-bottom:1px solid #fff}
.card .btn{background:var(--green);font-family:"Marcellus",serif;font-size:8px;padding:6px 14px;text-transform:uppercase}
.card-golf{left:136px;background:linear-gradient(160deg,#b79b43 0%,#6c7a2c 60%,#3f5c25 100%)}
.card-golf h3::before,.card-golf h3::after{width:32px}
.card-club{left:311px;background:linear-gradient(180deg,#2e2f3f 0%,#3f3b3a 60%,#2b2a2b 100%)}
.card-wedding{left:487px;background:linear-gradient(180deg,#3a3030 0%,#6b4f3e 60%,#a98b72 100%)}

.testimonials{left:0;top:890px;width:788px;height:177px}
.testimonials h2{position:absolute;top:36px;width:100%;text-align:center;font-family:"Marcellus",serif;font-weight:400;font-size:16px;text-transform:uppercase;letter-spacing:.5px}
.quote{left:180px;top:68px;width:446px;font-size:8.5px;line-height:14px;color:#555}
.quote-mark{left:152px;top:54px;font-family:"Marcellus",serif;font-size:40px;color:#ccc;line-height:1}
.arrows{left:383px;top:132px;display:flex;gap:3px}
.arrows span{width:12px;height:12px;border:1px solid var(--green);display:flex;align-items:center;justify-content:center}

.footer{left:0;top:1067px;width:788px;height:109px;background:var(--dark);color:var(--footer-text)}
.col{top:14px;font-size:6.5px;line-height:12px}
.col h4{font-weight:600;font-size:7.5px;text-transform:uppercase;color:#fff;margin-bottom:4px}
.col ul{list-style:none}
.social{display:flex;gap:3px;margin-top:4px}
.social span{width:11px;height:11px;background:#fff}
.map{left:451px;top:30px;width:88px;height:60px;background:linear-gradient(135deg,#e9e5dc 0%,#d7e4cf 60%,#a9c7e4 100%)}
.footer-brand{left:552px;top:42px;display:flex;align-items:center;gap:5px;color:#555}
.footer-brand .brand-mark{width:14px;height:14px;background:#555}
.footer-brand .brand-name{font-family:"Marcellus",serif;font-size:12px}
.bottom-bar{left:0;top:1176px;width:788px;height:24px;background:var(--bar);font-size:6px;color:#666}
.bottom-bar .copy{left:136px;top:8px}
.bottom-bar .legal{right:145px;top:8px}
</style>
</head>
<body>
  <header class="hero abs" role="img" aria-label="Rendering of the club pool terrace with cabanas, umbrellas and lawns"></header>
  <div class="hero-brand abs"><span class="brand-mark"></span><span class="brand-name">Sage Meadow<br>Country Club</span></div>
  <h1 class="headline abs serif"><span class="l1">Family, Community and the Highest</span><span class="l2">Ideals of the Game of Golf</span></h1>
  <div class="scroll abs">Scrolls<br>Down</div>

  <nav class="nav abs">
    <div class="nav-brand abs"><span class="brand-mark"></span><span class="brand-name">Sage Meadow</span></div>
    <ul class="nav-links abs">
      <li>Guest Info</li><li>Membership</li><li>Golf</li><li>Club House &amp; Amenities</li><li>Wedding &amp; Events</li>
    </ul>
  </nav>

  <section class="intro abs">
    <h2>These are the enduring values of Sage Meadow Country Club.</h2>
    <p class="lead">Perched on a ridge with inspiring views of the Los Angeles basin and folded within the valleys of Sage Meadow Estates, Sage Meadow Country Club is the finest private club in Palos Verdes, and all of the South Bay.</p>
    <p>With an atmosphere that inspires a deep sense of camaraderie among the membership and reinforces great traditions from generation to generation, Sage Meadow Country Club is a place where parents and children, friends and neighbors come together to eat, play, and enjoy life.</p>
  </section>
  <div class="rendering abs" role="img" aria-label="Watercolor rendering of the new clubhouse among trees"></div>
  <p class="established abs">Established in 1965</p>

  <section class="features abs">
    <div class="card card-golf abs" role="img" aria-label="Golfer on the green at sunset"><h3><span>Golf</span></h3><span class="btn">Click Here</span></div>
    <div class="card card-club abs" role="img" aria-label="Clubhouse exterior at dusk"><h3><span>Club House &amp;<br>Amenities</span></h3><span class="btn">Click Here</span></div>
    <div class="card card-wedding abs" role="img" aria-label="Evening reception under string lights"><h3><span>Wedding &amp;<br>Events</span></h3><span class="btn">Click Here</span></div>
  </section>

  <section class="testimonials abs">
    <h2>Experience Say About Us</h2>
    <div class="quote-mark abs">&ldquo;</div>
    <p class="quote abs">Curabitur consequat imperdiet metus et tincidunt. Mauris vel luctus sapien. Nunc semper, magna eget finibus aliquam, eros arcu aliquet urna, nec ultrices ex nisl ac tellus. Curabitur consequat imperdiet metus et tincidunt. Mauris vel luctus sapien. Nunc semper, magna eget finibus aliquam, eros arcu aliquet urna, nec ultrices ex nisl ac tellus.</p>
    <div class="arrows abs">
      <span><svg width="6" height="8" viewBox="0 0 6 8"><path d="M5 1L1 4l4 3" fill="none" stroke="#5aa51c" stroke-width="1.5"/></svg></span>
      <span><svg width="6" height="8" viewBox="0 0 6 8"><path d="M1 1l4 3-4 3" fill="none" stroke="#5aa51c" stroke-width="1.5"/></svg></span>
    </div>
  </section>

  <footer class="footer abs">
    <div class="col abs" style="left:138px"><h4>Navigation</h4><ul><li>Guest Info</li><li>Membership</li><li>Golf</li><li>Club House &amp; Amenities</li><li>Wedding &amp; Events</li></ul></div>
    <div class="col abs" style="left:235px"><h4>Clubhouse &amp; Amenities</h4><ul><li>Dining</li><li>Fitness</li><li>Aquatics</li><li>Tennis</li><li>Spa</li></ul></div>
    <div class="col abs" style="left:340px"><h4>Contact Us</h4><p>Sage Meadow Country Club<br>12 Meadowlark Lane, SME 90000.</p><h4 style="margin-top:6px">Follow Us On</h4><div class="social"><span></span><span></span><span></span></div></div>
    <div class="map abs" role="img" aria-label="Location map of the club"></div>
    <div class="footer-brand abs"><span class="brand-mark"></span><span class="brand-name">Sage Meadow</span></div>
  </footer>
  <div class="bottom-bar abs"><span class="copy abs">© 2016 Sage Meadow All Rights Reserved.</span><span class="legal abs">Terms of Service | Privacy Policy</span></div>
</body>
</html>
```